Friendwall landing page design

We are a Video Production Company and plan to launch our Business Fan Page soon. We are running a competition and need a design done for the related Friendwall landing page.

The landing page should have the following copy:

Win a Web Video Advertisement Worth $4000!
To enter you must:
1. Vote for the web video advertisement that you enjoy the most (check out the Poll Tab)
2. "Like" our Friendwall Fan Page
3. Explain what an ideal web video advertisement would look like for your business (Post this on our wall)
Conditions apply so check out the Poll tab for more information. Competition ends June 30th so get voting!

I have included some previous marketing material for reference only. You do not need to use this as a style a guide
Updates

Target Market(s)

Business owners or marketing managers

Requirements
Must have
• Lofty Crane-media Logo
web address included: www.loftycm.example
An image needs to accompany the copy
Should not have
• text only

```html
<!DOCTYPE html>
<html lang="en">
<head>
<meta charset="utf-8">
<title>Win a Web Video Advertisement — Lofty Crane-media</title>
<link href="https://fonts.googleapis.com/css2?family=Archivo+Black&family=Arimo:wght@400;700&display=swap" rel="stylesheet">
<style>
  :root {
    --navy: #0b3f7c;
    --blue: #1769b8;
    --sky: #2d8fd8;
    --ice: #dbeefa;
    --pale: #eef7fd;
    --band: #c3e2f6;
    --orange: #f7941d;
    --ink: #1b2a3a;
    --white: #ffffff;
  }
  * { box-sizing: border-box; margin: 0; padding: 0; }
  html, body { width: 694px; height: 1200px; overflow: hidden; background: var(--white); }
  body { font-family: "Arimo", Arial, sans-serif; color: var(--ink); }
  .page { position: relative; width: 694px; height: 1200px; }

  .top-bar {
    height: 60px; display: flex; align-items: center; justify-content: center; gap: 10px;
    background: linear-gradient(#2a79c4, var(--navy));
    color: var(--white); font-weight: 700; font-size: 26px;
  }
  .like-chip {
    display: inline-flex; align-items: center; height: 28px; padding: 0 12px;
    background: linear-gradient(#f6f8fb, #dfe5ee); border: 1px solid #9aa8bd; border-radius: 4px;
    color: #3b4f74; font-size: 16px; font-weight: 700;
  }

  .hero { position: relative; height: 476px; overflow: hidden; }
  .hero-visual {
    position: absolute; inset: 0;
    background:
      radial-gradient(ellipse at 55% 30%, #e8f5ff 0%, #9fd1f3 25%, transparent 55%),
      linear-gradient(160deg, #3e9be0 0%, #1e6fc0 45%, #0d4c96 100%);
  }
  .headline {
    position: absolute; left: 0; right: 0; top: 262px;
    text-align: center; font-family: "Archivo Black", "Arial Black", sans-serif;
    color: var(--white); font-size: 52px; line-height: 1.02; text-transform: uppercase;
    transform: rotate(-6deg) skewX(-6deg);
    text-shadow: 0 3px 0 var(--navy), 0 5px 10px rgba(0,0,0,.45);
  }
  .headline .amount { color: var(--orange); }

  .enter-title {
    height: 64px; display: flex; align-items: center; justify-content: center;
    background: var(--band); color: var(--blue); font-weight: 700; font-size: 34px;
  }
  .steps { list-style: none; }
  .step { display: flex; margin-top: 6px; }
  .step-1 { height: 124px; }
  .step-2 { height: 112px; }
  .step-3 { height: 120px; }
  .step-number {
    width: 110px; display: flex; align-items: center; justify-content: center;
    background: var(--band); color: var(--blue); font-weight: 700; font-size: 54px;
  }
  .step-text {
    flex: 1; display: flex; align-items: center; gap: 14px; padding: 0 28px;
    background: var(--pale); color: var(--navy); font-weight: 700; font-size: 22px; line-height: 1.3;
  }
  .step-text.large { font-size: 30px; }
  .step-text .like-chip { height: 40px; font-size: 20px; padding: 0 16px; }

  .conditions {
    margin-top: 12px; text-align: center; font-size: 17px; line-height: 1.35; color: var(--ink);
  }

  .footer {
    position: absolute; left: 0; right: 0; bottom: 0; height: 132px;
    display: flex; align-items: center; justify-content: space-between; padding: 0 24px;
    border-top: 4px solid var(--band);
  }
  .brand { display: flex; align-items: center; gap: 10px; color: var(--blue); font-weight: 700; font-size: 22px; }
  .brand-dot { width: 22px; height: 22px; border-radius: 50%; background: var(--sky); }
  .web-address {
    display: flex; align-items: center; justify-content: center;
    width: 360px; height: 76px; border-radius: 12px;
    background: linear-gradient(#2e86d2, var(--navy)); color: var(--white);
    font-weight: 700; font-size: 28px;
  }
</style>
</head>
<body>
<main class="page">
  <header class="top-bar">Click on the <span class="like-chip">Like</span> button above</header>

  <section class="hero">
    <div class="hero-visual" role="img" aria-label="Curving arrow sweeping past a fan of glowing video screens on a blue background"></div>
    <h1 class="headline">Win a web video<br>advertisement<br>worth <span class="amount">$4000!</span></h1>
  </section>

  <h2 class="enter-title">To Enter You Must</h2>
  <ol class="steps">
    <li class="step step-1">
      <span class="step-number">1</span>
      <p class="step-text">Vote for the web video advertisement that you enjoy the most (check out the Poll Tab)</p>
    </li>
    <li class="step step-2">
      <span class="step-number">2</span>
      <p class="step-text large"><span class="like-chip">Like</span> Our Friendwall Fan Page</p>
    </li>
    <li class="step step-3">
      <span class="step-number">3</span>
      <p class="step-text">Explain what an ideal web video advertisement would look like for your business (Post this on our wall)</p>
    </li>
  </ol>

  <p class="conditions">Conditions apply so check out the Poll tab for more information.<br>Competition ends June 30th so get voting!</p>

  <footer class="footer">
    <div class="brand"><span class="brand-dot"></span>Lofty Crane-media</div>
    <div class="web-address">www.loftycm.example</div>
  </footer>
</main>
</body>
</html>
```